Packaging for a Herbal Coffee Brand

We need packaging for a herbal coffee brand. I want the packaging to be fun, bright and have some image of coffee drink (NO BEANS as it does not contain coffee) on it.

The product is called Coffee Substitute. It's gluten-free, acid-free and caffeine free

Ingredients
organic roasted chicory powder, organic roasted carob powder, and organic roasted dandelion root powder

Preparation Instructions - Coffee Press or Tea Straner

1. For each 6 oz of water add 1-2 heaping teaspoons of Zest coffee substitute to a coffee press or tea strainer (add more or less water depending on your strength preference)
2. Pour hot water—not quite boiling—into the pot/cup, and gently stir
3. Let stand for 10-15 seconds then press the plunger down slowly, or remove the strainer.
4. Zest and enjoy! (see what we did there?)

"Use By" line: Best if used within 6 months of opening

Statements regarding dietary supplements have not been evaluated by the BHQ and are not intended to diagnose, treat, cure, or prevent any disease or health condition.

Target Market(s)

Health oriented women who can not drink coffee but want to enjoy the flavor of it.

Font styles to use
Sans Serif

Requirements
Must have
• An image of coffee. I'm cool if this is graphics or literally a cup of coffee on it.

some inspiration:
https://weareloma.example/collections/bestsellers/products/original-loma
https://vornikfoods.example/products/new-product-quikmix

Please make sure to follow these rules when designing per our printer - https://trundowrap.example/wp-content/uploads/2020/02/Prepress-Checklist-Rev9.pdf Standard Stand up pouch - that is Height x Width x Gusset: 9 x 6 x 3-1/2 inches 230 x 150 x 90 mm Location of Zipper (Bottom-of-Bag to Bottom-of-Zipper): 7-5/8 inches or 192 mm See this also https://trundowrap.example/wp-content/uploads/2020/02/LR-Submitting-Artwork-Guidelines-Side-to-Side-Registration.pdf
Nice to have
• Really FUN, BOLD,
Should not have
• Boring, plain, NO coffee beans. Should be CLEAR that it is a coffee substitute

```html
<!DOCTYPE html>
<html lang="en">
<head>
<meta charset="utf-8">
<title>Zest Herbals – Coffee Substitute Label</title>
<link rel="stylesheet" href="https://fonts.googleapis.com/css2?family=Marcellus&family=Quicksand:wght@400&display=swap">
<style>
  :root {
    --backdrop: #c2c2c2;
    --label-white: #ffffff;
    --roast-brown: #2e1411;
    --latte-tan: #c8b08e;
    --saucer-cream: #ece5d6;
    --cup-shade: #6b5340;
  }
  html, body {
    margin: 0;
    padding: 0;
    width: 1200px;
    height: 835px;
    overflow: hidden;
    background: var(--backdrop);
  }
  .canvas {
    position: relative;
    width: 1200px;
    height: 835px;
  }
  .pouch-label {
    position: absolute;
    left: 380px;
    top: 40px;
    width: 440px;
    height: 754px;
    display: block;
  }
  .brand-name {
    font-family: "Marcellus", serif;
    fill: var(--roast-brown);
    text-anchor: middle;
  }
  .product-title {
    font-family: "Marcellus", serif;
    fill: var(--label-white);
    text-anchor: middle;
  }
  .claim-text {
    font-family: "Quicksand", sans-serif;
    font-weight: 400;
    fill: var(--label-white);
    text-anchor: middle;
    font-size: 20px;
  }
  .claim-icon circle,
  .claim-icon path,
  .claim-icon line {
    fill: none;
    stroke: var(--label-white);
    stroke-width: 2.2;
    stroke-linecap: round;
  }
</style>
</head>
<body>
<main class="canvas">
  <svg class="pouch-label" viewBox="0 0 627 1073" xmlns="http://www.w3.org/2000/svg">
    <defs>
      <linearGradient id="cup-photo-tones" x1="0" y1="0" x2="1" y2="1">
        <stop offset="0" stop-color="var(--saucer-cream)"/>
        <stop offset="1" stop-color="var(--cup-shade)"/>
      </linearGradient>
    </defs>

    <rect class="label-ground" x="0" y="0" width="627" height="1073" fill="var(--label-white)"/>

    <polygon class="hex-band" points="0,268 313,196 627,268 627,830 313,905 0,838" fill="var(--roast-brown)"/>
    <polygon class="hex-keyline" points="12,280 313,210 615,280 615,820 313,891 12,826"
             fill="none" stroke="var(--label-white)" stroke-width="2"/>

    <g class="brand-badge">
      <circle cx="313" cy="172" r="114" fill="var(--latte-tan)"/>
      <circle cx="313" cy="172" r="109" fill="var(--label-white)"/>
      <circle cx="313" cy="172" r="103" fill="var(--latte-tan)"/>
      <text class="brand-name" x="313" y="180" font-size="70">Zest</text>
      <text class="brand-name" x="313" y="240" font-size="34">Herbals</text>
    </g>

    <text class="product-title" x="313" y="433" font-size="112">COFFEE</text>
    <text class="product-title" x="313" y="510" font-size="72">SUBSTITUTE</text>

    <g class="claim-icon" transform="translate(180 585)">
      <circle r="23"/>
      <line x1="0" y1="-14" x2="0" y2="14"/>
      <path d="M0 -6 l-6 -5 M0 -6 l6 -5 M0 2 l-6 -5 M0 2 l6 -5"/>
      <line x1="-16" y1="-16" x2="16" y2="16"/>
    </g>
    <text class="claim-text" x="180" y="640">gluten</text>
    <text class="claim-text" x="180" y="664">free</text>

    <g class="claim-icon" transform="translate(313 585)">
      <circle r="23"/>
      <path d="M-2 -15 c0 8 10 4 10 14 c0 9 -8 13 -14 9 c-5 -3 -2 -8 -6 -10"/>
    </g>
    <text class="claim-text" x="313" y="640">acid</text>
    <text class="claim-text" x="313" y="664">free</text>

    <g class="claim-icon" transform="translate(445 585)">
      <circle r="23"/>
      <circle r="17"/>
      <path d="M-7 6 c-2 -10 4 -16 14 -16 c0 10 -6 16 -14 16 z"/>
      <line x1="-12" y1="-12" x2="12" y2="12"/>
    </g>
    <text class="claim-text" x="445" y="640">caffeine</text>
    <text class="claim-text" x="445" y="664">free</text>

    <g class="cup-medallion">
      <circle cx="313" cy="878" r="170" fill="var(--latte-tan)"/>
      <circle cx="313" cy="878" r="161" fill="var(--label-white)"/>
      <circle cx="313" cy="878" r="152" fill="var(--latte-tan)"/>
      <circle class="cup-photo" cx="313" cy="878" r="130" fill="url(#cup-photo-tones)"
              role="img" aria-label="Photo placeholder: top-down view of a cup of dark coffee substitute on a cream saucer"/>
    </g>
  </svg>
</main>
</body>
</html>
```